Electrical Contractor double sided A6 flyer

I need a flyer designed for two distinct markets: Domestic customers & Commercial/Industrial customers.
One side of card would be for Domestic customers and would include LED lighting; Consumer Units replacement: Repairs; No Job too small plus quillbox logo website address.
Other side of card would be for Industrial/commercial customers and would include: Electrical condition reports; Installations; Repairs; control panel design & build (I use neo sans standard font). I want the card to be bold and distintive and the sort of theing youll want to stick on the fridge or pin on a board and not throw away.
Updates

Sorry guys, I forgot to say landscape please not portrait. Added Friday, June 10, 2016

Target Market(s)

Domestic customers & Industrial / Commercial businesses

Industry/Entity Type

Contractor

Font styles to use
Other font styles liked:
• neo sans

Requirements
Must have
• Phone number; website address; quillbox logo
Nice to have
• QR code if it fits in wuith the design

```html
<!DOCTYPE html>
<html lang="en">
<head>
<meta charset="utf-8">
<title>Quillbox Electrical Ltd – Flyer</title>
<link rel="stylesheet" href="https://fonts.googleapis.com/css2?family=Cabin:ital,wght@0,400;0,500;0,600;0,700;1,400;1,500&display=swap">
<style>
  :root {
    --green: #2fa82a;
    --green-light: #6fd65a;
    --ink: #222;
    --grey: #555;
    --silver-1: #f2f2f2;
    --silver-2: #c9c9c9;
    --gold-1: #f4ecdc;
    --gold-2: #d8c8a8;
  }
  * { box-sizing: border-box; margin: 0; padding: 0; }
  html, body { width: 851px; height: 1200px; overflow: hidden; background: #fff; }
  body { position: relative; font-family: "Cabin", "Trebuchet MS", sans-serif; color: var(--ink); }

  .card {
    position: absolute; left: 33px; width: 785px; overflow: hidden;
    box-shadow: 0 0 8px rgba(0,0,0,.45);
  }
  .card--domestic { top: 33px; height: 555px;
    background: radial-gradient(circle at 70% 40%, #ffffff 0%, var(--silver-1) 40%, var(--silver-2) 100%); }
  .card--commercial { top: 610px; height: 557px;
    background: radial-gradient(circle at 70% 40%, #fbf6ea 0%, var(--gold-1) 45%, var(--gold-2) 100%); }

  .photo { position: absolute; inset: 0; }
  .card--domestic .photo {
    clip-path: polygon(0 0, 402px 0, 477px 100%, 0 100%);
    background:
      radial-gradient(circle at 210px 360px, rgba(255,120,80,.9) 0, rgba(200,60,40,.5) 40px, rgba(60,40,60,.4) 120px, transparent 200px),
      linear-gradient(180deg, #000 0%, #0b0b14 55%, #3a3a55 100%);
  }
  .card--commercial .photo {
    clip-path: polygon(0 0, 407px 0, 467px 100%, 0 100%);
    background:
      radial-gradient(ellipse at 240px 240px, rgba(255,190,80,.95) 0, rgba(210,130,40,.7) 80px, rgba(90,70,30,.5) 180px, transparent 260px),
      linear-gradient(160deg, #5a5a30 0%, #3a3420 50%, #15120c 100%);
  }

  .tagline { position: absolute; color: var(--green-light); white-space: nowrap; }
  .card--domestic .tagline {
    left: 42px; top: 44px; font-size: 22.5px; font-style: italic; line-height: 30px;
  }
  .card--commercial .tagline {
    left: 25px; top: 437px; font-size: 21px; font-weight: 700; line-height: 27px;
    text-shadow: 1px 1px 2px #000;
  }

  .badge { position: absolute; width: 130px; height: 72px; }
  .card--domestic .badge { left: 40px; top: 153px; }
  .card--commercial .badge { left: 322px; top: 342px; width: 108px; height: 60px; }

  .brand { position: absolute; display: flex; align-items: center; gap: 10px; }
  .brand__mark { width: 40px; height: 40px; border-radius: 50%; background: var(--green); flex: none; }
  .brand__name { font-size: 21px; font-weight: 700; letter-spacing: .3px; color: var(--ink); white-space: nowrap; }
  .address { position: absolute; font-size: 13.5px; color: var(--grey); }
  .phone, .web { position: absolute; display: flex; align-items: center; gap: 8px; color: var(--green); }
  .phone { font-size: 27px; font-weight: 700; }
  .web { font-size: 21px; }
  .phone svg, .web svg { flex: none; }
  .rule { position: absolute; height: 2px; background: #444; }

  .section-title { position: absolute; color: var(--green); font-weight: 700; text-transform: uppercase; text-align: center; }
  .services { position: absolute; list-style: none; }
  .services li { display: flex; align-items: flex-start; gap: 10px; white-space: nowrap; }
  .services svg { flex: none; margin-top: 5px; }

  .card--domestic .services li { font-size: 20px; font-weight: 600; text-transform: uppercase; line-height: 25px; color: #333; }
  .card--commercial .services li { font-size: 20px; font-weight: 600; font-variant: small-caps; line-height: 27px; color: #333; }

  .promise { position: absolute; color: var(--green); font-weight: 700; font-size: 17px; }
  .coverage { position: absolute; text-align: center; font-style: italic; font-size: 19.5px; line-height: 27px; color: var(--grey); }
</style>
</head>
<body>

<section class="card card--domestic">
  <div class="photo" role="img" aria-label="Photo of a glowing light bulb lying on its side on a dark reflective surface"></div>
  <p class="tagline">A full range of top quality<br>electrical services at a price<br>homeowners can afford!</p>
  <svg class="badge" viewBox="0 0 130 72" aria-hidden="true"><rect x="2" y="2" width="126" height="68" rx="4" fill="none" stroke="#cfcfcf" stroke-width="3"/></svg>

  <div class="brand" style="left:430px; top:50px;"><span class="brand__mark"></span><span class="brand__name">QUILLBOX ELECTRICAL LTD</span></div>
  <p class="address" style="left:488px; top:100px;">14 Marsh Lane, Ferndale, FD4 2QX</p>
  <p class="phone" style="left:488px; top:128px;">
    <svg width="22" height="18" viewBox="0 0 22 18" aria-hidden="true"><path d="M1 6c0-3 4-5 10-5s10 2 10 5l-4 1-1-2H6L5 7z" fill="#333"/><rect x="4" y="8" width="14" height="9" rx="2" fill="#333"/></svg>01632 960418</p>
  <p class="web" style="left:490px; top:165px;">
    <svg width="18" height="18" viewBox="0 0 18 18" aria-hidden="true"><circle cx="9" cy="9" r="7.5" fill="none" stroke="#555" stroke-width="1.5"/><path d="M1.5 9h15M9 1.5c-4 4-4 11 0 15M9 1.5c4 4 4 11 0 15" fill="none" stroke="#555" stroke-width="1.2"/></svg>quillbox-electrical.co.uk</p>
  <div class="rule" style="left:457px; top:202px; width:310px;"></div>
  <h2 class="section-title" style="left:457px; top:218px; width:310px; font-size:17.5px;">Domestic Electrical Services</h2>
  <ul class="services" style="left:500px; top:253px;">
    <li><svg width="14" height="14" viewBox="0 0 14 14" aria-hidden="true"><path d="M1 13 6 6l2 3 5-8" fill="none" stroke="#444" stroke-width="2"/></svg>Electrical Repairs</li>
    <li><svg width="14" height="14" viewBox="0 0 14 14" aria-hidden="true"><path d="M1 13 6 6l2 3 5-8" fill="none" stroke="#444" stroke-width="2"/></svg>New Installations</li>
    <li><svg width="14" height="14" viewBox="0 0 14 14" aria-hidden="true"><path d="M1 13 6 6l2 3 5-8" fill="none" stroke="#444" stroke-width="2"/></svg>Consumer Unit<br>Upgrades</li>
    <li><svg width="14" height="14" viewBox="0 0 14 14" aria-hidden="true"><path d="M1 13 6 6l2 3 5-8" fill="none" stroke="#444" stroke-width="2"/></svg>LED Lighting</li>
    <li><svg width="14" height="14" viewBox="0 0 14 14" aria-hidden="true"><path d="M1 13 6 6l2 3 5-8" fill="none" stroke="#444" stroke-width="2"/></svg><span style="text-transform:none">and MORE!</span></li>
  </ul>
  <p class="promise" style="left:518px; top:423px;">NO JOB IS TOO SMALL!</p>
  <p class="coverage" style="left:470px; top:448px; width:310px;">We provide a full range of<br>services in Ferndale and<br>the surrounding areas</p>
</section>

<section class="card card--commercial">
  <div class="photo" role="img" aria-label="Close-up photo of a vintage filament bulb glowing amber in front of a wheel-shaped fitting"></div>
  <svg class="badge" viewBox="0 0 108 60" aria-hidden="true"><rect x="2" y="2" width="104" height="56" rx="4" fill="none" stroke="#e0e0e0" stroke-width="3"/></svg>
  <p class="tagline">Our reputation for being a highly skilled<br>electrical contractor in Ferndale is<br>backed up by the clients we work with!</p>

  <div class="brand" style="left:432px; top:52px;"><span class="brand__mark"></span><span class="brand__name">QUILLBOX ELECTRICAL LTD</span></div>
  <p class="address" style="left:490px; top:102px;">14 Marsh Lane, Ferndale, FD4 2QX</p>
  <p class="phone" style="left:490px; top:131px;">
    <svg width="22" height="18" viewBox="0 0 22 18" aria-hidden="true"><path d="M1 6c0-3 4-5 10-5s10 2 10 5l-4 1-1-2H6L5 7z" fill="#333"/><rect x="4" y="8" width="14" height="9" rx="2" fill="#333"/></svg>01632 960418</p>
  <p class="web" style="left:492px; top:167px;">
    <svg width="18" height="18" viewBox="0 0 18 18" aria-hidden="true"><circle cx="9" cy="9" r="7.5" fill="none" stroke="#555" stroke-width="1.5"/><path d="M1.5 9h15M9 1.5c-4 4-4 11 0 15M9 1.5c4 4 4 11 0 15" fill="none" stroke="#555" stroke-width="1.2"/></svg>quillbox-electrical.co.uk</p>
  <div class="rule" style="left:472px; top:227px; width:293px;"></div>
  <h2 class="section-title" style="left:472px; top:236px; width:293px; font-size:18px; line-height:30px;">Commercial &amp; Industrial<br>Electrical Services</h2>
  <ul class="services" style="left:490px; top:318px;">
    <li><svg width="14" height="14" viewBox="0 0 14 14" aria-hidden="true"><path d="M1 13 6 6l2 3 5-8" fill="none" stroke="#444" stroke-width="2"/></svg>Electrical condition<br>reports</li>
    <li><svg width="14" height="14" viewBox="0 0 14 14" aria-hidden="true"><path d="M1 13 6 6l2 3 5-8" fill="none" stroke="#444" stroke-width="2"/></svg>Installations</li>
    <li><svg width="14" height="14" viewBox="0 0 14 14" aria-hidden="true"><path d="M1 13 6 6l2 3 5-8" fill="none" stroke="#444" stroke-width="2"/></svg>Repairs &amp; maintenance</li>
    <li><svg width="14" height="14" viewBox="0 0 14 14" aria-hidden="true"><path d="M1 13 6 6l2 3 5-8" fill="none" stroke="#444" stroke-width="2"/></svg>control panel design<br>&amp; build</li>
    <li><svg width="14" height="14" viewBox="0 0 14 14" aria-hidden="true"><path d="M1 13 6 6l2 3 5-8" fill="none" stroke="#444" stroke-width="2"/></svg>and more!</li>
  </ul>
</section>

</body>
</html>
```